依頼詳細
不動産物件情報の冊子の表紙デザインです。春号らしいイメージと、簡単には捨てられないインパクトのあるデザインをお願いします。
※参考まで前号(冬号)の表紙を添付いたします
会社WEB:http://meridel-works.jp/
※必ずしも、前号のイメージにとらわれる必要はありません
記載項目
タイトル「物件情報 2020 春号」 会社ロゴ:添付参照 10周年記念タイトル:添付参照
希望イメージ
シンプル 複雑
単色 カラフル
暗い 明るい
日常 高級
遊び心 厳粛
未来的 伝統的
女性的 男性的
希望する色
設定なし
納品ファイル
• 高解像度JPG (.jpg)
• イラストレーター形式 (.ai)
補足説明
四半期に一度発行予定ですので、継続して発行して行きます
■ 選んだ理由

最終選考の4案中、一番投票が多かったです。
春の都会をうまく表現したデザインで、表紙にふさわしいと決定しました

■ 提案者全員のお礼・コメント

ご提案いただいた、多数の皆様、誠にありがとうございます。
また、次号の募集にもご参加いただければ幸いです

```html
<!DOCTYPE html>
<html lang="ja">
<head>
<meta charset="utf-8">
<title>物件情報 2020 春</title>
<link href="https://fonts.googleapis.com/css2?family=Noto+Serif+JP:wght@400;600&family=Cormorant+Garamond:wght@500&display=swap" rel="stylesheet">
<style>
  :root {
    --night: #1d2a6b;
    --violet: #4a4ca8;
    --blossom: #e98ab4;
    --glow: #e8324f;
    --white: #ffffff;
    --tile-light: rgba(255,255,255,0.85);
    --tile-lilac: rgba(205,200,240,0.75);
    --tile-navy: rgba(40,50,140,0.85);
    --tile-pink: rgba(240,190,215,0.7);
  }
  html, body { margin: 0; padding: 0; overflow: hidden; }
  body { width: 849px; height: 1200px; background: var(--night); }
  .cover { position: relative; width: 849px; height: 1200px; overflow: hidden; font-family: "Noto Serif JP", serif; color: var(--white); }
  .cover-photo {
    position: absolute; inset: 0;
    background:
      radial-gradient(ellipse 18% 45% at 50% 100%, rgba(255,80,100,0.95), transparent 70%),
      radial-gradient(ellipse 45% 40% at 5% 65%, rgba(240,140,185,0.9), transparent 70%),
      radial-gradient(ellipse 40% 40% at 98% 60%, rgba(240,140,185,0.85), transparent 70%),
      radial-gradient(ellipse 40% 30% at 50% 85%, rgba(200,40,80,0.8), transparent 75%),
      linear-gradient(180deg, #1b2468 0%, #3a3f9a 35%, #6a58a8 55%, #7a3a78 80%, #5a1838 100%);
  }
  .tiles { position: absolute; inset: 0; }
  .title {
    position: absolute; left: 500px; top: 30px; margin: 0;
    font-size: 118px; font-weight: 600; line-height: 136px; letter-spacing: 6px;
  }
  .issue { position: absolute; left: 500px; top: 420px; width: 300px; }
  .issue-rule { height: 1px; background: var(--white); }
  .issue-row { display: flex; align-items: center; height: 116px; }
  .issue-year { font-family: "Cormorant Garamond", serif; font-size: 46px; line-height: 1; letter-spacing: 4px; }
  .issue-season { font-family: "Cormorant Garamond", serif; font-size: 24px; letter-spacing: 5px; margin-top: 4px; }
  .issue-divider { width: 1px; height: 76px; background: var(--white); margin: 0 18px; }
  .issue-kanji { font-size: 56px; font-weight: 600; }
  .tagline { position: absolute; top: 990px; width: 100%; text-align: center; font-size: 20px; letter-spacing: 3px; margin: 0; }
  .brand { position: absolute; top: 1030px; left: 0; width: 100%; display: flex; justify-content: center; align-items: center; gap: 16px; }
  .brand-mark { width: 48px; height: 48px; border-radius: 50%; background: var(--white); }
  .brand-name { font-size: 46px; font-weight: 600; letter-spacing: 2px; }
  .anniversary { position: absolute; top: 1140px; left: 0; width: 100%; display: flex; justify-content: center; align-items: center; gap: 14px; }
  .anniversary-text { font-size: 14px; letter-spacing: 1px; }
  .anniversary-badge { width: 48px; height: 48px; border-radius: 50%; background: #c9a94e; }
</style>
</head>
<body>
<main class="cover">
  <div class="cover-photo" role="img" aria-label="夜景の川沿いに咲く桜並木と、ライトアップされた川面と都会のビル群"></div>

  <svg class="tiles" width="849" height="1200" viewBox="0 0 849 1200" aria-hidden="true">
    <rect x="0" y="0" width="85" height="85" fill="var(--tile-navy)"/>
    <rect x="85" y="0" width="85" height="85" fill="var(--tile-lilac)"/>
    <rect x="170" y="0" width="85" height="85" fill="var(--tile-navy)"/>
    <rect x="255" y="0" width="85" height="85" fill="var(--tile-light)"/>
    <rect x="340" y="0" width="85" height="85" fill="var(--tile-navy)"/>
    <rect x="0" y="85" width="85" height="85" fill="var(--tile-lilac)"/>
    <rect x="85" y="85" width="85" height="85" fill="var(--tile-navy)"/>
    <rect x="170" y="85" width="85" height="85" fill="var(--tile-lilac)"/>
    <rect x="340" y="85" width="85" height="85" fill="var(--tile-lilac)"/>
    <rect x="0" y="170" width="85" height="85" fill="var(--tile-navy)"/>
    <rect x="85" y="170" width="85" height="85" fill="var(--tile-light)"/>
    <rect x="0" y="255" width="85" height="85" fill="var(--tile-lilac)"/>
    <rect x="0" y="425" width="85" height="85" fill="var(--tile-pink)"/>
    <rect x="0" y="595" width="85" height="85" fill="var(--tile-pink)"/>
    <rect x="764" y="425" width="85" height="85" fill="var(--tile-pink)"/>
    <rect x="679" y="595" width="85" height="85" fill="var(--tile-pink)"/>
    <rect x="764" y="680" width="85" height="85" fill="var(--tile-pink)"/>
    <rect x="594" y="765" width="85" height="85" fill="var(--tile-pink)"/>
    <rect x="679" y="850" width="85" height="85" fill="var(--tile-pink)"/>
  </svg>

  <h1 class="title">物件<br>情報</h1>

  <div class="issue">
    <div class="issue-rule"></div>
    <div class="issue-row">
      <div>
        <div class="issue-year">2020</div>
        <div class="issue-season">SPRING</div>
      </div>
      <div class="issue-divider"></div>
      <div class="issue-kanji">春</div>
    </div>
    <div class="issue-rule"></div>
  </div>

  <p class="tagline">不動産で九州・東京・アジアを繋げる！</p>

  <div class="brand">
    <span class="brand-mark"></span>
    <span class="brand-name">Meridel Works</span>
  </div>

  <div class="anniversary">
    <span class="anniversary-text">株式会社メリデルは、おかげさまで10周年を迎えます</span>
    <span class="anniversary-badge"></span>
  </div>
</main>
</body>
</html>
```